BrewDune Lane.

I want the full logo on one side. And the other side the card if right Ralf the logo the left half orange like the car in the logo color with Lorena J Torvand
Founder and CEO
Email symbol then ltorvand@brewdunelanex.com
Www symbol. Then Brewdunelanex.com
Phone symbol then 555-214-BREW
The very bottom would like Brew Dune Lane is a division of Tumbler Treks. LLC

```html
<!DOCTYPE html>
<html lang="en">
<head>
<meta charset="utf-8">
<title>Brew Dune Lane – Business Cards</title>
<link rel="stylesheet" href="https://fonts.googleapis.com/css2?family=Open+Sans:ital,wght@0,400;0,600;0,700;1,400&display=swap">
<style>
  :root {
    --bg-top: #e4e6e8;
    --bg-bottom: #c9cbce;
    --card: #ffffff;
    --orange: #e08a24;
    --ink: #1d1d1d;
    --ink-soft: #333333;
    --rule: #555555;
  }
  * { box-sizing: border-box; margin: 0; padding: 0; }
  html, body {
    width: 1200px; height: 800px; overflow: hidden;
    font-family: "Open Sans", Arial, sans-serif;
    background: linear-gradient(160deg, var(--bg-top), var(--bg-bottom));
  }
  .stage {
    width: 1200px; height: 800px;
    display: flex; flex-direction: column; align-items: center; justify-content: center;
    gap: 30px;
  }
  .card {
    position: relative;
    width: 630px; height: 360px;
    background: var(--card);
    box-shadow: 0 6px 18px rgba(0,0,0,.18);
  }
  .brand {
    display: flex; align-items: center; justify-content: center; gap: 12px;
    font-weight: 700; color: var(--ink);
    letter-spacing: .5px;
  }
  .brand-dot {
    width: 18px; height: 18px; border-radius: 50%;
    background: var(--orange);
  }
  .card-front .brand {
    position: absolute; inset: 0;
    font-size: 50px;
  }
  .card-front .brand-dot { width: 30px; height: 30px; }
  .card-back .brand {
    position: absolute; top: 58px; left: 0; right: 0;
    font-size: 36px;
  }
  .details {
    position: absolute; top: 178px; left: 0; right: 0;
    display: flex; justify-content: center; align-items: stretch;
  }
  .person {
    text-align: right; padding-right: 22px;
    border-right: 1.5px solid var(--rule);
  }
  .person-name { color: var(--orange); font-weight: 700; font-size: 21px; line-height: 1.2; }
  .person-title { color: var(--ink-soft); font-size: 17px; }
  .contacts { list-style: none; padding-left: 22px; font-size: 16px; color: var(--ink); }
  .contacts li { display: flex; align-items: center; gap: 8px; line-height: 1.45; }
  .contacts svg { width: 14px; height: 14px; flex: none; }
  .division-band {
    position: absolute; left: 0; right: 0; top: 268px; height: 46px;
    background: var(--orange);
    display: flex; align-items: center; justify-content: center;
    color: #fff; font-style: italic; font-size: 17px;
  }
</style>
</head>
<body>
<main class="stage">
  <section class="card card-front" aria-label="Card front">
    <div class="brand"><span class="brand-dot"></span>Brew Dune Lane</div>
  </section>

  <section class="card card-back" aria-label="Card back">
    <div class="brand"><span class="brand-dot"></span>Brew Dune Lane</div>

    <div class="details">
      <div class="person">
        <p class="person-name">Lorena J Torvand</p>
        <p class="person-title">Founder and CEO</p>
      </div>
      <ul class="contacts">
        <li>
          <svg viewBox="0 0 24 24" aria-hidden="true"><path fill="#e08a24" d="M6.6 10.8a15 15 0 0 0 6.6 6.6l2.2-2.2c.3-.3.7-.4 1-.2 1.1.4 2.3.6 3.6.6.6 0 1 .4 1 1V20c0 .6-.4 1-1 1A17 17 0 0 1 3 4c0-.6.4-1 1-1h3.5c.6 0 1 .4 1 1 0 1.3.2 2.5.6 3.6.1.3 0 .7-.2 1z"/></svg>
          555-214-BREW
        </li>
        <li>
          <svg viewBox="0 0 24 24" aria-hidden="true"><rect x="2.5" y="5" width="19" height="14" fill="none" stroke="#e08a24" stroke-width="2"/><path d="M3 6l9 7 9-7" fill="none" stroke="#e08a24" stroke-width="2"/></svg>
          ltorvand@brewdunelanex.com
        </li>
        <li>
          <svg viewBox="0 0 24 24" aria-hidden="true"><g fill="none" stroke="#e08a24" stroke-width="2"><circle cx="12" cy="12" r="9.5"/><ellipse cx="12" cy="12" rx="4" ry="9.5"/><path d="M2.5 12h19M4 7h16M4 17h16"/></g></svg>
          Brewdunelanex.com
        </li>
      </ul>
    </div>

    <div class="division-band">Brew Dune Lane is a division of Tumbler Treks. LLC</div>
  </section>
</main>
</body>
</html>
```